Poster for teenagers

Bright, trendy, modern and young fonts - a variety of fonts, plus arrows and clip art (no photos) for an A3 size poster to be hung in study halls of schools. There are six dot points. I think each point should be in some kind of box or circle.

Here are a few ideas of the kind of thing I mean.
http://www.varrowdale.example.gov.au/Page/Images/youth_Advisory_Group_Poster_(1).jpg

http://www.brindlecourt.example/sites/default/files/Youth-Panel-Poster-1-Web.jpg

http://www.quillmarsh.example.org.au/images/librariesprovider4/Misc-illustrations/140335-qui-youth-superheros-heroup-highres.jpg?sfvrsn=0

https://pkrvworldwide.files.examplehost.com/2013/04/544477_432153653542694_970534114_n.jpg

Also my logo should be on it some where . I've attached a my logo.

Here is the text:
How to get organised and motivated this year.
1. Write stuff down
Write down things you need to do and when you plan to do them. Use digital calendars, to do apps and email lists – or pen and paper. Even if you are sure you will remember – get it out of your head and onto paper/your phone/laptop. You are more likely to get it done and feel less stressed.
2. Set up habits
If you do things in the same way, at the same time or after the same thing – then after a few weeks, it becomes much easier to get those things done. Set up a particular time, or place to do study tasks – or link them with another daily task. EG: art homework every Tuesday. Violin practice after breakfast.
3. Focus!
For 15-30 minutes at a time - totally focus on homework. Put your phone away, log out of chatterloop, close down other programs and really concentrate. Then have a break, send a text or whatever – and then go back to focussed study. Fifteen minutes of concentrated study gets more achieved than an hour of study switching back and forth between homework and other activities.
4. Just do something
No motivation? Just take a “bite”. Set a timer and just do 5 minutes. Or 15. Or read just the first two pages. Or the first problem on the worksheet. Something is better than nothing – and sometimes once you start, it’s easier to keep going.
5. Use rewards and consequences
Reward yourself when you do a hard task and use consequences when you don’t. Use food, fun activities, gaming and social time to motivate yourself – you get it when you do tasks, you don’t when you don’t. EG 15 minutes of clipstream when I finish this page. Tell other people your plans and you are more likely to stick to them.
6. Imagine the future
When you really can’t be find any motivation to do the things you need to do – take 30 seconds to think about what will happen in a week, month and year if you get on with it. What will happen then and how will that feel. And imagine what will happen in a week, month and year if you DON’T do those things – and how will that feel.

Good luck !
For free articles and one to one help with study skills, increasing motivation, coping with stress or tough times in senior school, go to tallowbrook.example.net.au
Tallow Brook Psychology and Education

```html
<!DOCTYPE html>
<html lang="en">
<head>
<meta charset="utf-8">
<title>Getting Organised, Getting Motivated</title>
<link rel="stylesheet" href="https://fonts.googleapis.com/css2?family=Oswald:wght@500;600&family=Quando&display=swap">
<style>
  :root {
    --red-top: #ff1a10;
    --red-bottom: #ff3a12;
    --red-ink: #f0200f;
    --white: #ffffff;
    --disc: #e1e5e4;
    --disc-edge: #c9cfce;
    --ring: #d9a3b9;
  }
  * { margin: 0; padding: 0; box-sizing: border-box; }
  html, body { width: 844px; height: 1200px; overflow: hidden; }
  body {
    background: linear-gradient(180deg, var(--red-top), var(--red-bottom));
    position: relative;
    font-family: "Quando", Georgia, serif;
    color: var(--white);
  }
  .title-banner { position: absolute; left: 0; top: 0; }
  .tip {
    position: absolute;
    font-size: 16.6px;
    line-height: 24px;
    color: var(--white);
  }
  .badge {
    position: absolute;
    border-radius: 50%;
    background: var(--disc);
    border: 2px solid var(--disc-edge);
    display: flex;
    flex-direction: column;
    align-items: center;
    justify-content: center;
    text-align: center;
    font-family: "Oswald", "Arial Narrow", sans-serif;
    font-weight: 500;
    color: var(--red-ink);
    text-transform: uppercase;
    line-height: 1.02;
    z-index: 2;
  }
  .badge::before {
    content: "";
    position: absolute;
    inset: 6px;
    border-radius: 50%;
    border: 2px solid var(--ring);
  }
  .badge span { display: block; position: relative; }
  .sign-off {
    position: absolute;
    left: 0; width: 844px; top: 1038px;
    text-align: center;
    font-family: "Oswald", "Arial Narrow", sans-serif;
    font-weight: 500;
    font-size: 50px;
    line-height: 60px;
  }
  .footer-note {
    position: absolute;
    left: 0; width: 844px; top: 1102px;
    text-align: center;
    font-size: 12.6px;
    line-height: 20px;
  }
  .org-name {
    position: absolute;
    left: 0; width: 844px; top: 1156px;
    text-align: center;
    font-size: 10px;
  }
</style>
</head>
<body>
  <svg class="title-banner" width="844" height="140" viewBox="0 0 844 140">
    <defs>
      <clipPath id="ribbon-clip"><polygon points="356,0 486,0 486,132 421,100 356,132"/></clipPath>
    </defs>
    <polygon points="356,0 486,0 486,132 421,100 356,132" fill="#ffffff"/>
    <text x="415" y="56" text-anchor="middle" textLength="490" lengthAdjust="spacingAndGlyphs" font-family="Oswald, sans-serif" font-weight="600" font-size="34" fill="#ffffff">GETTING ORGANISED, GETTING MOTIVATED</text>
    <text x="415" y="56" text-anchor="middle" textLength="490" lengthAdjust="spacingAndGlyphs" font-family="Oswald, sans-serif" font-weight="600" font-size="34" fill="#f0200f" clip-path="url(#ribbon-clip)">GETTING ORGANISED, GETTING MOTIVATED</text>
  </svg>

  <div class="badge" style="left:16px;top:125px;width:180px;height:180px;font-size:34px;"><span>Write</span><span>Stuff</span><span>Down</span></div>
  <p class="tip" style="left:214px;top:152px;width:610px;">Write down things you need to do and when you plan to do them. Use digital calendars, to do apps and email lists – or pen and paper. Even if you are sure you will remember – get it out of your head and onto paper/your phone/laptop. You are more likely to get it done and feel less stressed.</p>

  <div class="badge" style="left:68px;top:285px;width:162px;height:162px;font-size:44px;line-height:0.98;"><span>Set Up</span><span>Habits</span></div>
  <p class="tip" style="left:244px;top:307px;width:585px;">If you do things in the same way, at the same time or after the same thing – then after a few weeks, it becomes much easier to get those things done. Set up a particular time, or place to do study tasks – or link them with another daily task. EG: art homework every Tuesday. Violin practice after breakfast.</p>

  <div class="badge" style="left:0px;top:432px;width:162px;height:162px;font-size:44px;"><span>Focus!</span></div>
  <p class="tip" style="left:172px;top:448px;width:660px;">For 15-30 minutes at a time - totally focus on homework. Put your phone away, log out of chatterloop, close down other programs and really concentrate. Then have a break, send a text or whatever – and then go back to focussed study. Fifteen minutes of concentrated study gets more achieved than an hour of study switching back and forth between homework and other activities.</p>

  <div class="badge" style="left:18px;top:565px;width:168px;height:168px;font-size:32px;"><span>Just Do</span><span>Something</span></div>
  <p class="tip" style="left:200px;top:608px;width:625px;">No motivation? Just take a “bite”. Set a timer and just do 5 minutes. Or 15. Or read just the first two pages. Or the first problem on the worksheet. Something is better than nothing – and sometimes once you start, it’s easier to keep going.</p>

  <div class="badge" style="left:28px;top:705px;width:164px;height:164px;font-size:22px;line-height:1;"><span>Use</span><span style="font-size:34px;">Rewards</span><span style="font-size:17px;">and</span><span style="font-size:20px;">Consequences</span></div>
  <p class="tip" style="left:207px;top:722px;width:620px;">Reward yourself when you do a hard task and use consequences when you don’t. Use food, fun activities, gaming and social time to motivate yourself – you get it when you do tasks, you don’t when you don’t. EG 15 minutes of clipstream when I finish this page. Tell other people your plans and you are more likely to stick to them.</p>

  <div class="badge" style="left:26px;top:855px;width:186px;height:186px;font-size:46px;line-height:0.98;"><span>Imagine</span><span style="font-size:34px;">the</span><span>Future</span></div>
  <p class="tip" style="left:237px;top:880px;width:595px;">When you really can’t be find any motivation to do the things you need to do – take 30 seconds to think about what will happen in a week, month and year if you get on with it. What will happen then and how will that feel. And imagine what will happen in a week, month and year if you DON’T do those things – and how will that feel.</p>

  <h2 class="sign-off">GOOD LUCK</h2>
  <p class="footer-note">For free articles and one to one help with study skills, increasing motivation, coping with stress or tough times in senior school, go to<br>tallowbrook.example.net.au</p>
  <p class="org-name">Tallow Brook Psychology and Education</p>
</body>
</html>
```